以下のイメージでデザインをお願いいたします。
ご提案の際には、デザインに込めた意味合いも、お書き添えいただけるとうれしいです。

・シンプル、かつスタイリッシュ、また、親しみやすさがありながらも、品格があるデザイン
・アフリカのポップアートも扱いますが、事業内容は多岐に渡るため、ポップな感じだけの名刺はNG
・名刺の向きはタテ型でも横型でもOK
・「会社として大事にしていることや目標」に加えて、「成長していく」、「飛躍する」イメージを込めていただいたデザイン
・名刺を配布する先はBtoBで、当面は日本の企業様が対象
⇒CSR(社会貢献活動)に力をいれている企業や消費財を扱う企業の方々に訴求していきたいと思っています。
企業の担当者としてはマーケティングや営業関係、役員クラス、経営者などを想定しています。
・印刷用紙はマット系
■表面(日本語):名前(ダミー)、肩書き(CEO & Co-Founder)、会社名、住所(ダミー)、HP URL(ダミー)、e-mail(ダミー)、携帯電話番号(ダミー)

■裏面(英語):名前(ダミー)、肩書き(CEO & Co-Founder)、会社名、住所(ダミー)、HP URL(ダミー)、e-mail(ダミー)、携帯電話番号(ダミー 、+81を付けてください)
ロゴにあるオレンジ、グレー、白の3色を使用する
▼事業内容
・デジタルコンテンツの企画・制作及び販売・輸出入
・絵画その他美術品等の販売及び輸出入
・ライセンス管理及びライセンス許諾事業
・学術、文化、芸術又はスポーツの振興を図る活動
このたびは、弊社の名刺コンペにご参加いただきありがとうございます。
たくさんの素晴らしいご提案をいただき、感謝しております。
これから選定に入らせていただきたいと思います。年末年始をはさみますので、恐れ入りますが、1月4日頃を目処に発表させていただきたく存じます。
ご参加いただいたデザイナー、クリエイターの皆様に重ねて御礼申し上げます。
どうぞ良い年をお迎えくださいませ。

金賞:morning57様
シンプルで飽きのこないデザインで、ロゴと社名のバランスが絶妙でした。また、裏面も表とは違う表情を演出してあり好感をもちました。

銀賞:
r-opa様
透かし模様のロゴが秀逸でした。裏面は色合いを変えてくださったバージョンが素敵でした。

hiroe48様
パズルのピース部分を抜き出した使い方が個性的でインパクトがありました。

このたびは、弊社の名刺コンペにご参加いただきありがとうございました。
ロゴを活かしてくださるすばらしいデザインばかりで、提案をいただくのがとても楽しみでした。
全てのご提案にコメントをお返ししきれず、心苦しいかぎりです。
今後も、デザイン募集の依頼をさせていただくことがあるかと存じますが、ぜひまた応募をいただければ幸いです。
応募いただいたデザイナーの皆様に、この場を借りて、改めて御礼申し上げます。今後ともよろしくお願い申し上げます。

```html
<!DOCTYPE html>
<html lang="ja">
<head>
<meta charset="utf-8">
<title>Tessera Holdings – Business Card</title>
<link rel="stylesheet" href="https://fonts.googleapis.com/css2?family=Noto+Serif:wght@700&family=Noto+Sans+JP:wght@400;500;700&display=swap">
<style>
  :root {
    --orange: #e8741e;
    --peach: #f6c9a3;
    --peach-light: #fbe6d4;
    --ink: #3a3a3a;
    --heading-ink: #4a3f38;
    --grey: #9a9a9a;
    --grey-light: #e3e3e3;
    --paper: #ffffff;
    --page: #ffffff;
  }
  * { margin: 0; padding: 0; box-sizing: border-box; }
  html, body { width: 880px; height: 1200px; overflow: hidden; background: var(--page); }
  body { position: relative; font-family: "Noto Sans JP", sans-serif; color: var(--ink); }

  .side-title {
    position: absolute; left: 30px;
    font-family: "Noto Serif", serif; font-weight: 700;
    font-size: 50px; letter-spacing: 0.5px; line-height: 1; white-space: nowrap;
  }
  .side-title--front { top: 18px; color: var(--heading-ink); }
  .side-title--back { top: 676px; color: var(--orange); }

  .card {
    position: absolute; left: 30px; width: 820px;
    background: var(--paper); overflow: hidden;
    box-shadow: 4px 6px 10px rgba(0,0,0,0.35);
  }
  .card--front { top: 82px; height: 475px; }
  .card--back { top: 750px; height: 420px; }
  .card__bg { position: absolute; inset: 0; width: 100%; height: 100%; }

  .brand-mark {
    position: absolute; display: flex; flex-direction: column; align-items: center; gap: 10px;
    color: var(--orange); font-weight: 700; font-size: 24px;
  }
  .brand-mark__dot { width: 90px; height: 90px; border-radius: 50%; background: var(--orange); }
  .card--front .brand-mark { left: 55px; top: 50px; }
  .card--back .brand-mark { left: 55px; top: 35px; }

  .person { position: absolute; right: 70px; text-align: left; white-space: nowrap; z-index: 1; }
  .person__role { font-size: 16px; color: var(--ink); letter-spacing: 1px; }
  .person__name { font-weight: 500; color: var(--ink); line-height: 1.2; }
  .card--front .person { top: 110px; }
  .card--front .person__name { font-size: 34px; letter-spacing: 10px; margin-top: 10px; padding-bottom: 6px; border-bottom: 1px solid var(--grey); }
  .card--back .person { top: 130px; }
  .card--back .person__role { letter-spacing: 3px; }
  .card--back .person__name { font-size: 34px; letter-spacing: 4px; margin-top: 4px; }

  .contact { position: absolute; left: 42px; z-index: 1; }
  .contact__company { font-weight: 700; font-size: 22px; margin-bottom: 10px; white-space: nowrap; }
  .contact__row { display: flex; align-items: baseline; gap: 16px; line-height: 1.45; white-space: nowrap; }
  .contact__key { width: 20px; font-weight: 700; color: var(--orange); font-size: 24px; }
  .contact__value { font-size: 16px; }
  .contact__value--tel { font-size: 24px; letter-spacing: 5px; }
  .card--front .contact { top: 240px; }
  .card--back .contact { top: 270px; }
  .card--back .contact__company { font-weight: 500; margin-bottom: 4px; }
  .card--back .contact__value--tel { font-size: 22px; letter-spacing: 3px; }

  .faint-disc {
    position: absolute; right: 25px; top: 250px; width: 140px; height: 140px;
    border-radius: 50%; background: var(--peach); opacity: 0.3;
  }
</style>
</head>
<body>
  <h1 class="side-title side-title--front">Tessera Holdings Co.,Ltd.</h1>

  <section class="card card--front">
    <svg class="card__bg" viewBox="0 0 820 475" preserveAspectRatio="none" aria-hidden="true">
      <defs>
        <linearGradient id="front-band" x1="0" y1="0" x2="1" y2="0">
          <stop offset="0" stop-color="#f6c9a3"/>
          <stop offset="1" stop-color="#fbe6d4"/>
        </linearGradient>
      </defs>
      <path d="M0 250 C 250 200, 520 290, 820 225 L820 475 L0 475 Z" fill="url(#front-band)"/>
      <path d="M0 232 C 260 180, 520 275, 820 205" fill="none" stroke="#f6c9a3" stroke-width="3" opacity="0.7"/>
    </svg>
    <div class="brand-mark"><span class="brand-mark__dot"></span><span>Tessera</span></div>
    <div class="person">
      <p class="person__role">CEO &amp; Co-Founder</p>
      <p class="person__name">佐藤 花子</p>
    </div>
    <div class="contact">
      <p class="contact__company">株式会社テッセラ・ホールディングス</p>
      <p class="contact__row"><span class="contact__key">T</span><span class="contact__value contact__value--tel">090 2468 1357</span></p>
      <p class="contact__row"><span class="contact__key">E</span><span class="contact__value">h-sato@tessera-h.example</span></p>
      <p class="contact__row"><span class="contact__key">A</span><span class="contact__value">150-0001 東京都渋谷区神宮前●●3-18 ●●ビル 4F</span></p>
    </div>
  </section>

  <h2 class="side-title side-title--back">Tessera Holdings Co.,Ltd.</h2>

  <section class="card card--back">
    <svg class="card__bg" viewBox="0 0 820 420" preserveAspectRatio="none" aria-hidden="true">
      <path d="M0 265 C 260 205, 540 290, 820 235 L820 420 L0 420 Z" fill="#e3e3e3"/>
      <path d="M0 248 C 270 190, 540 275, 820 218" fill="none" stroke="#e3e3e3" stroke-width="4"/>
    </svg>
    <span class="faint-disc" aria-hidden="true"></span>
    <div class="brand-mark"><span class="brand-mark__dot"></span><span>Tessera</span></div>
    <div class="person">
      <p class="person__role">CEO &amp; Co-Founder</p>
      <p class="person__name">Hanako Sato</p>
    </div>
    <div class="contact">
      <p class="contact__company">Tessera Holdings Co.,Ltd.</p>
      <p class="contact__row"><span class="contact__key">T</span><span class="contact__value contact__value--tel">+81 90 2468 1357</span></p>
      <p class="contact__row"><span class="contact__key">M</span><span class="contact__value">h-sato@tessera-h.example</span></p>
      <p class="contact__row"><span class="contact__key">A</span><span class="contact__value">●● Bld.4F, ●●3-18, Jingumae, Shibuya-ku, Tokyo, 150-0001, Japan</span></p>
    </div>
  </section>
</body>
</html>
```